Brazilian wine business need a label for a sparkling wine

We are importing a new italian sparkling wine, but we need to build our own brand. Our main focus is to sell sparkling wine for events, specially for weddings. So, specially for this audience, presentation is key.
We like to see wine in a "uncomplicated" way.
It is a mid price product.
The foil capsule color must be black, white or silver, due to production restrictions. We cannot have any graphic interference in this part, also.

We need to develop a label for it. The name will be "Lucenti Brut" (means "hug" in italian).

Our main public is people around the early 30s, so it should look modern and clean.
It is good, but not mandatory, to have a few information at the front label:
- Alcohol % (12%)
- Origin (Italy)

We need to avoid a few colours, for different reasons:
- Don´t use yellow/orange: too linked to Maison Dorvalle;
- Don´t use red or pink: people think it is a rosé, but it is a white.
Our idea is to work with white and blue or turquoise, maybe a green, something like that. Can have a touch of gold, also. (more references in the color tab below)
- The bottle is black.

Industry/Entity Type

Business

Font styles to use
Other font styles liked:
• Berlin Sans FB Regular or something less "round" but similar to Cooper Black Regular

Colors
00a990
33b8a4

Requirements
Must have
• As the name means "hug", we want to have a graphic symbol that represents connections, alliances, symbiosis or infinite. I attached a few symbols that could be explore, but of course you can bring differente suggestions.
• We need a clean design, nothing with too many information.

```html
<!DOCTYPE html>
<html lang="en">
<head>
<meta charset="utf-8">
<title>Lucenti Brut – Label</title>
<link rel="stylesheet" href="https://fonts.googleapis.com/css2?family=Poiret+One&display=swap">
<style>
  :root {
    --page: #ffffff;
    --teal: #22b5a0;
    --label-white: #ffffff;
    --gold-deep: #c9962c;
    --gold-mid: #e8c25a;
    --gold-light: #fff6cf;
    --ink: #111111;
  }
  html, body {
    margin: 0;
    padding: 0;
    width: 1131px;
    height: 1200px;
    overflow: hidden;
    background: var(--page);
  }
  .canvas {
    position: relative;
    width: 1131px;
    height: 1200px;
  }
  .label-art {
    position: absolute;
    inset: 0;
    width: 1131px;
    height: 1200px;
  }
  .label-title {
    font-family: "Poiret One", sans-serif;
    font-size: 56px;
    fill: var(--ink);
    letter-spacing: 0.5px;
  }
  .label-facts {
    font-family: "Poiret One", sans-serif;
    font-size: 23px;
    font-weight: 400;
    fill: var(--ink);
  }
  .rings-emblem {
    position: absolute;
    left: 500px;
    top: 545px;
    width: 196px;
    height: 110px;
    border-radius: 50%;
    background: radial-gradient(ellipse at 45% 45%, var(--gold-light) 0%, var(--gold-mid) 45%, var(--gold-deep) 75%, rgba(255,255,255,0) 100%);
  }
</style>
</head>
<body>
<main class="canvas">
  <svg class="label-art" viewBox="0 0 880 934" xmlns="http://www.w3.org/2000/svg">
    <defs>
      <linearGradient id="gold-sweep" x1="0" y1="0" x2="1" y2="0">
        <stop offset="0" stop-color="var(--gold-mid)"/>
        <stop offset="0.3" stop-color="var(--gold-light)"/>
        <stop offset="0.6" stop-color="var(--gold-deep)"/>
        <stop offset="1" stop-color="var(--gold-light)"/>
      </linearGradient>
    </defs>
    <rect class="label-frame" x="181" y="81" width="563" height="709"
          fill="var(--teal)" stroke="url(#gold-sweep)" stroke-width="8"/>
    <path class="label-panel"
          d="M208,97 Q463,200 717,97 Q659,435 717,773 Q463,683 208,773 Q282,435 208,97 Z"
          fill="var(--label-white)" stroke="url(#gold-sweep)" stroke-width="3.5"/>
    <text class="label-title" x="463" y="400" text-anchor="middle">Lucenti Brut</text>
    <text class="label-facts" x="463" y="709" text-anchor="middle">alc. 12% vol • Origin Italy</text>
  </svg>
  <div class="rings-emblem" role="img" aria-label="Two interlocked gold wedding rings"></div>
</main>
</body>
</html>
```